Retro 80's Vinyl Wrap Design for RV Protector Shade

As part of a full restoration, I need to reproduce a design of a retro graphic for an 80's Australian caravan (a 'trailer' in the USA), which will be printed on vinyl and applied to a front protector shade on the caravan.
I am looking for an accurate reproduction of the original design, using similar colours to those used in the past. (EDIT: I have a design submitted that satisfies the reproduction brief. To save people doing exactly the same thing. I am now only looking for original designs, as per the description below).
I'm happy to consider designs that reflect the original 80's design, but show a fresh perspective for those that would like to get creative. This might be a modern take that reflects the period, or perhaps a design that the designer of the day might have gone with if they had the technology we have today to reproduce it in vinyl (the original was hand painted, so had to be kept simple to reproduce it easily). A simple brief is to capture the fun and the vibe of the late 70's/early 80's, as this is what we plan to do in the whole restoration. Any creative design should try to incorporate the green and gold on the side of the van, as these will be retained through the restoration. Preference will be given to a design that can keep the 'Coast Roamer' text in its original font (Bookman Std Italic, customised) and original position position, so other people familiar with the van can recognise the reference to the original design. Search for 'marlowe coast roamer decal' and you'll see plenty examples of the original text online.
In the attached files you'll find a picture of our early 80's caravan that is being restored. In the image the protector shade is painted with two angled stripes and the white has yellowed, and has been highlighted in the image with two red arrows, just to be clear. That is the area I will be covering with this design (printed to vinyl). Also attached are examples of the original design I am looking to reproduce.
The protector shade is 2110mm wide, and 570mm high. Included in these measurements is the aluminium trim around the protector shade, which is 25mm wide.
EDIT: An image named profile.png has been added. This shows a close up of the protector shade the vinyl wrap will be applied to. This is to show the profile of the aluminium sheet the protector shade is made from. The pitch (the distance between two crowns, which effectively is the same distance over one crown and one trough) is 100mm. It is recommended bleed is allowed for in any design. If the design is intended to align a particular distance from the edge of a crown or trough, it is recommended additional bleed is allowed for top and bottom, allowing extra vertical movement so the vinyl can be positioned correctly,

```html
<!DOCTYPE html>
<html lang="en">
<head>
<meta charset="utf-8">
<title>Coast Roamer – Protector Shade Wrap Layout</title>
<link rel="stylesheet" href="https://fonts.googleapis.com/css2?family=Libre+Baskerville:wght@700&display=swap">
<style>
  :root {
    --paper: #ffffff;
    --frame: #b9babe;
    --green: #94cb66;
    --gold: #ecc840;
    --ink: #231f20;
  }
  html, body {
    margin: 0;
    padding: 0;
    width: 1200px;
    height: 567px;
    overflow: hidden;
    background: var(--paper);
  }
  .layout-sheet {
    display: block;
    width: 1200px;
    height: 567px;
  }
  .shade-frame { fill: var(--paper); stroke: var(--frame); stroke-width: 19; }
  .band-green { fill: var(--green); }
  .band-gold { fill: var(--gold); }
  .van-name {
    font-family: "Libre Baskerville", "Bookman Old Style", serif;
    font-weight: 700;
    font-size: 64px;
    fill: var(--ink);
  }
  .dim-line { stroke: var(--ink); stroke-width: 1.4; fill: none; }
  .dim-head { fill: var(--ink); }
  .dim-label {
    font-family: "Libre Baskerville", "Bookman Old Style", serif;
    font-weight: 700;
    font-size: 20px;
    fill: var(--ink);
  }
</style>
</head>
<body>
<svg class="layout-sheet" viewBox="0 0 2000 945" xmlns="http://www.w3.org/2000/svg">
  <!-- shade panel with aluminium trim -->
  <rect class="shade-frame" x="149.5" y="266.5" width="1601" height="417"/>

  <!-- stripe bands -->
  <path class="band-green" d="M159 329 H1600 A146 146 0 0 1 1725 435 H159 Z"/>
  <path class="band-green" d="M159 515 H1725 A146 146 0 0 1 1600 622 H159 Z"/>
  <path class="band-gold" d="M159 382 H1480 A93 93 0 0 1 1566 435 H159 Z"/>
  <path class="band-gold" d="M159 515 H1566 A93 93 0 0 1 1480 569 H159 Z"/>

  <!-- van name -->
  <text class="van-name" x="1718" y="500" text-anchor="end">Coast Roamer</text>

  <!-- overall width -->
  <line class="dim-line" x1="150" y1="240" x2="1750" y2="240"/>
  <path class="dim-head" d="M140 240 L162 232 L162 248 Z"/>
  <path class="dim-head" d="M1760 240 L1738 232 L1738 248 Z"/>
  <text class="dim-label" x="983" y="230" text-anchor="middle">2110 mm</text>

  <!-- overall height -->
  <line class="dim-line" x1="119" y1="267" x2="119" y2="683"/>
  <path class="dim-head" d="M119 257 L111 279 L127 279 Z"/>
  <path class="dim-head" d="M119 693 L111 671 L127 671 Z"/>
  <text class="dim-label" x="62" y="466" text-anchor="middle">570mm</text>

  <text class="dim-label" x="140" y="726">Frame: 25mm wide(around)</text>

  <!-- band spacing ticks -->
  <g class="band-ticks">
    <path class="dim-line" d="M1770 275 H1803 M1770 329 H1803 M1770 382 H1803 M1770 435 H1803 M1770 515 H1803 M1770 569 H1803 M1770 622 H1803 M1770 675 H1803"/>
    <path class="dim-head" d="M1762 275 l20 -7 v14 Z M1762 329 l20 -7 v14 Z M1762 382 l20 -7 v14 Z M1762 435 l20 -7 v14 Z M1762 515 l20 -7 v14 Z M1762 569 l20 -7 v14 Z M1762 622 l20 -7 v14 Z M1762 675 l20 -7 v14 Z"/>
    <path class="dim-line" d="M1803 275 L1862 302 L1803 329 M1803 329 L1862 355 L1803 382 M1803 382 L1862 408 L1803 435 M1803 435 L1860 475 L1803 515 M1803 515 L1862 542 L1803 569 M1803 569 L1862 595 L1803 622 M1803 622 L1862 648 L1803 675"/>
    <text class="dim-label" x="1865" y="310">69.33 mm</text>
    <text class="dim-label" x="1865" y="363">69.33 mm</text>
    <text class="dim-label" x="1865" y="416">69.33 mm</text>
    <text class="dim-label" x="1863" y="484">104 mm</text>
    <text class="dim-label" x="1865" y="550">69.33 mm</text>
    <text class="dim-label" x="1865" y="603">69.33 mm</text>
    <text class="dim-label" x="1865" y="656">69.33 mm</text>
  </g>
</svg>
</body>
</html>
```